Childcare Centre trifold brochure

Design a contemporary trifold brochure for a childcare centre that meets Australian printing requirements with supplied content, logo's, fonts and photo's. Please refer to the attached DL flyer front and back for similar possible style and content.

Target Market(s)

Families

Industry/Entity Type

Childcare

Requirements
Must have
• refer attached content, photo's, logo's and examples. Colours should be same as Pantone purple and green and or variations of. Refer attached dl flyer example.

```html
<!DOCTYPE html>
<html lang="en">
<head>
<meta charset="utf-8">
<title>Bright Sprouts – Trifold Brochure</title>
<link href="https://fonts.googleapis.com/css2?family=Baloo+2:wght@600;800&family=Open+Sans:wght@400;600&family=Kalam:wght@700&display=swap" rel="stylesheet">
<style>
  :root{
    --purple:#8e1f8e;
    --purple-dark:#6d1570;
    --green:#3aa935;
    --green-dark:#2a8a2a;
    --ink:#3a3a3a;
    --paper:#ffffff;
    --grey:#eeeeef;
    --stage:#e6e6ea;
  }
  *{box-sizing:border-box;margin:0;padding:0}
  html,body{width:800px;height:1200px;overflow:hidden}
  body{background:var(--stage);font-family:"Open Sans",sans-serif;color:var(--ink);position:relative}
  .sheet{position:absolute;left:25px;width:750px;height:530px;display:flex;background:var(--paper);box-shadow:0 4px 14px rgba(0,0,0,.15)}
  .sheet--outside{top:40px}
  .sheet--inside{top:630px}
  .panel{position:relative;width:250px;height:100%;overflow:hidden}
  .panel+.panel{border-left:1px solid #e2e2e2}
  .wave{position:absolute;left:0;width:250px}
  .photo{position:absolute;left:14px;right:14px;border-radius:8px}
  .heading{font-family:"Baloo 2",sans-serif;font-weight:800;line-height:1.05}
  .script{font-family:"Kalam",cursive;font-weight:700}
  .body-text{font-size:8.5px;line-height:1.5}
  .light{color:#fff}

  /* Outside – welcome panel */
  .quote{position:absolute;top:18px;left:18px;right:18px}
  .quote__mark{font-family:"Baloo 2",sans-serif;font-size:52px;color:#cfcfd4;line-height:.6;display:block;height:24px}
  .quote__sign{color:var(--purple);font-size:15px;margin-top:4px}
  .quote__role{font-size:8px;color:#777}
  .curriculum{position:absolute;left:18px;right:18px;top:330px}
  .curriculum .heading{font-size:22px;margin-bottom:8px}

  /* Outside – contact panel */
  .partners{position:absolute;top:0;left:0;right:0;height:92px;background:var(--grey);display:flex;align-items:center;justify-content:center;gap:8px}
  .partners__name{font-family:"Baloo 2",sans-serif;font-weight:800;font-size:17px;color:var(--green)}
  .badge{width:26px;height:26px;background:#cfd0d6;border-radius:4px}
  .tagline{position:absolute;top:104px;left:18px;right:18px;text-align:center;color:var(--purple);font-size:20px;line-height:1.1}
  .contact{position:absolute;left:0;right:0;top:190px;bottom:0;background:var(--purple);padding:22px 20px 0;text-align:center;color:#fff}
  .contact .heading{font-size:20px;margin-bottom:6px}
  .contact p{font-size:9.5px;line-height:1.55}
  .contact .address{margin-top:12px}
  .enrol{margin-top:22px;font-family:"Baloo 2",sans-serif;font-weight:800;font-size:24px;line-height:1}
  .phone{font-family:"Baloo 2",sans-serif;font-weight:800;font-size:20px;display:flex;align-items:center;justify-content:center;gap:6px}
  .web{position:absolute;left:0;right:0;bottom:0;height:38px;background:var(--green);display:flex;align-items:center;justify-content:center;font-size:10px;font-weight:600}

  /* Outside – cover */
  .brand{position:absolute;top:22px;right:20px;display:flex;align-items:center;gap:8px}
  .brand__dot{width:22px;height:22px;border-radius:50%;background:var(--green)}
  .brand__name{font-family:"Baloo 2",sans-serif;font-weight:800;font-size:26px;color:var(--purple);line-height:1}
  .brand__sub{position:absolute;top:56px;right:20px;font-size:8px;color:#777}
  .cover-text{position:absolute;left:18px;right:18px;bottom:60px;text-align:center;color:#fff}
  .cover-text .heading{font-size:17px}
  .cover-text p{font-size:9px;margin-top:4px}

  /* Inside – FAQ */
  .faq{position:absolute;inset:0;background:var(--green)}
  .faq__title{position:absolute;top:34px;left:18px;right:18px;font-size:20px;color:#fff}
  .faq__list{position:absolute;top:82px;left:18px;right:18px;color:#fff}
  .faq__q{font-weight:600;font-size:9.5px;margin-top:10px}
  .faq__a{font-size:8.5px;line-height:1.5}
  .first-step{position:absolute;left:0;right:0;bottom:0;height:120px;background:var(--paper);padding:26px 18px 0}
  .first-step__lead{font-size:12px;color:var(--green-dark)}
  .first-step__main{font-size:30px;color:var(--green);line-height:1.1}

  /* Inside – kindergarten */
  .kinder{position:absolute;top:20px;left:18px;right:18px}
  .kinder .heading{font-size:14px;color:var(--purple)}
  .kinder .body-text{margin-top:8px}
  .fees{width:100%;border-collapse:collapse;margin-top:10px;font-size:8.5px}
  .fees th{background:var(--purple);color:#fff;text-align:left;padding:4px 5px;font-weight:600}
  .fees td{padding:4px 5px;border-bottom:1px solid #ddd}

  /* Inside – activities */
  .activities{position:absolute;left:18px;right:18px;top:300px;color:#fff}
  .activities .heading{font-size:22px;margin-bottom:8px}
</style>
</head>
<body>

<!-- Outside spread -->
<section class="sheet sheet--outside">
  <article class="panel panel--welcome">
    <div class="quote">
      <span class="quote__mark">“</span>
      <p class="body-text">Every child deserves a warm, safe place to play, learn and grow. Our educators nurture curiosity and confidence so each little learner can shine every day.</p>
      <p class="quote__sign script">Jane Holt</p>
      <p class="quote__role">Centre Director</p>
    </div>
    <div class="photo" style="top:170px;height:120px;background:linear-gradient(135deg,#c98a5a,#7fae5c 60%,#5b8ac2)" role="img" aria-label="Photo of children playing together outdoors"></div>
    <svg class="wave" style="top:280px;height:250px" viewBox="0 0 250 250" preserveAspectRatio="none" aria-hidden="true">
      <path d="M0 30 Q125 -10 250 25 L250 250 L0 250Z" fill="var(--green)"/>
      <path d="M0 40 Q125 0 250 35 L250 250 L0 250Z" fill="var(--purple)"/>
    </svg>
    <div class="curriculum light">
      <h2 class="heading">Our Curriculum</h2>
      <p class="body-text">Our play-based program follows the national early years framework, blending creative arts, music, outdoor discovery and early literacy. Small groups let educators tailor activities to every child's interests and pace.</p>
    </div>
  </article>

  <article class="panel panel--contact">
    <div class="partners">
      <span class="partners__name">Harbourview</span>
      <span class="badge"></span><span class="badge"></span>
    </div>
    <p class="tagline script">Not so little things<br>big things grow</p>
    <div class="contact">
      <h2 class="heading">Opening Hours</h2>
      <p>Monday – Friday<br>6:30am – 6:00pm<br>Closed public holidays</p>
      <p class="address">42 Wattle Grove Road<br>Pine Ridge QLD 4210</p>
      <p class="enrol">ENROL NOW</p>
      <p class="phone">
        <svg width="16" height="16" viewBox="0 0 24 24" aria-hidden="true"><path fill="#fff" d="M6.6 10.8a15 15 0 0 0 6.6 6.6l2.2-2.2c.3-.3.7-.4 1-.2 1.1.4 2.3.6 3.6.6.6 0 1 .4 1 1V20c0 .6-.4 1-1 1A17 17 0 0 1 3 4c0-.6.4-1 1-1h3.5c.6 0 1 .4 1 1 0 1.3.2 2.5.6 3.6.1.3 0 .7-.2 1z"/></svg>
        07 5550 0192
      </p>
      <div class="web">www.brightsprouts.com.au</div>
    </div>
  </article>

  <article class="panel panel--cover">
    <div class="brand"><span class="brand__dot"></span><span class="brand__name">Bright Sprouts</span></div>
    <p class="brand__sub">Early Learning Centre</p>
    <div class="photo" style="top:84px;height:250px;background:linear-gradient(160deg,#b9673f,#d9a56a 45%,#6e9a4c)" role="img" aria-label="Photo of children climbing on outdoor play equipment"></div>
    <svg class="wave" style="top:300px;height:230px" viewBox="0 0 250 230" preserveAspectRatio="none" aria-hidden="true">
      <path d="M0 40 Q140 0 250 30 L250 230 L0 230Z" fill="var(--green)"/>
      <path d="M0 55 Q140 15 250 45 L250 230 L0 230Z" fill="var(--purple)"/>
    </svg>
    <div class="cover-text">
      <h1 class="heading">Pine Ridge Early Learning Centre</h1>
      <p>42 Wattle Grove Road, Pine Ridge QLD 4210</p>
    </div>
  </article>
</section>

<!-- Inside spread -->
<section class="sheet sheet--inside">
  <article class="panel panel--faq">
    <div class="faq">
      <svg class="wave" style="top:0;height:60px" viewBox="0 0 250 60" preserveAspectRatio="none" aria-hidden="true">
        <path d="M0 0 L250 0 L250 10 Q120 40 0 24Z" fill="var(--purple)"/>
      </svg>
      <h2 class="faq__title heading">Frequently Asked Questions</h2>
      <div class="faq__list">
        <p class="faq__q">What should my child bring?</p>
        <p class="faq__a">A hat, water bottle, spare clothes and a comfort toy for rest time.</p>
        <p class="faq__q">Are meals provided?</p>
        <p class="faq__a">Yes, our cook prepares fresh, healthy meals and snacks daily.</p>
        <p class="faq__q">How do I enrol?</p>
        <p class="faq__a">Call us or visit the centre to book a tour and collect an enrolment pack.</p>
      </div>
      <div class="first-step">
        <p class="first-step__lead script">Getting ready for Kindergarten:</p>
        <p class="first-step__main script">The first step</p>
      </div>
    </div>
  </article>

  <article class="panel panel--kinder">
    <div class="kinder">
      <h2 class="heading">Choosing the right Kindergarten for you and your child is one of the most important decisions</h2>
      <p class="body-text">Our approved kindergarten program is led by qualified teachers and helps children build skills for a confident start to school.</p>
      <table class="fees">
        <tr><th>Room</th><th>Age</th><th>Days</th></tr>
        <tr><td>Nursery</td><td>0–2 yrs</td><td>Mon–Fri</td></tr>
        <tr><td>Toddlers</td><td>2–3 yrs</td><td>Mon–Fri</td></tr>
        <tr><td>Kindy</td><td>3–4 yrs</td><td>Mon–Fri</td></tr>
        <tr><td>Pre-Prep</td><td>4–5 yrs</td><td>Mon–Fri</td></tr>
      </table>
    </div>
    <div class="photo" style="top:300px;height:180px;background:linear-gradient(135deg,#e9c7a4,#f1a9b8 50%,#9fc7e8)" role="img" aria-label="Photo of smiling preschool children in a classroom"></div>
    <svg class="wave" style="bottom:0;height:70px" viewBox="0 0 250 70" preserveAspectRatio="none" aria-hidden="true">
      <path d="M0 30 Q125 0 250 25 L250 70 L0 70Z" fill="var(--green)"/>
      <path d="M0 44 Q125 14 250 40 L250 70 L0 70Z" fill="var(--purple)"/>
    </svg>
  </article>

  <article class="panel panel--activities">
    <div class="photo" style="top:18px;height:230px;background:linear-gradient(150deg,#f2c46a,#e88a5c 50%,#9b6fb8)" role="img" aria-label="Photo of a child painting at an easel"></div>
    <svg class="wave" style="top:250px;height:280px" viewBox="0 0 250 280" preserveAspectRatio="none" aria-hidden="true">
      <path d="M0 25 Q125 -5 250 20 L250 280 L0 280Z" fill="var(--green)"/>
      <path d="M0 38 Q125 8 250 33 L250 280 L0 280Z" fill="var(--purple)"/>
    </svg>
    <div class="activities">
      <h2 class="heading">Our Activities</h2>
      <p class="body-text">From sandpit adventures to story time, our days are full of hands-on fun. Children explore gardening, music, movement, cooking and art, building friendships and skills along the way.</p>
    </div>
  </article>
</section>

</body>
</html>
```